Youth Education Program for PRL

Looking for a high-end slick looking design for power-point and/or PDF. Quick turnaround of a Presentation of 10 slides for a meeting for an educational youth program. Information and recommended images will be provided for each slide. Each Slide other than cover should have a logo, header, footer, and page number. Design should be simple and modern with either graphic examples or images. Less is more. Websites for company is http://brightpathlearn.example/ and other images can be found on tandorcreative.example or you can use stock imagery you feel is good.
Colors
Designer to choose colors to be used in the design.
Look and feel
Each slider illustrates characteristics of the customer's brand and the style your logo design should communicate.

```html
<!DOCTYPE html>
<html lang="en">
<head>
<meta charset="utf-8">
<title>Our Company – BrightPath Youth Program</title>
<link rel="stylesheet" href="https://fonts.googleapis.com/css2?family=Jost:wght@400;500;600&display=swap">
<style>
  :root {
    --green: #8cc63f;
    --charcoal: #3a3a3a;
    --slate: #8a8a8a;
    --white: #ffffff;
    --backdrop: #2c2c2c;
    --body-grey: #7f7f7f;
    --logo-grey: #9d9d9d;
  }
  * { box-sizing: border-box; }
  html, body { margin: 0; padding: 0; overflow: hidden; background: var(--backdrop); }
  .slide {
    position: relative;
    width: 1200px;
    height: 676px;
    overflow: hidden;
    background: var(--backdrop);
    font-family: "Jost", "Futura", sans-serif;
  }
  .page-card {
    position: absolute;
    top: 0;
    bottom: 0;
    width: 400px;
    border-radius: 16px;
    box-shadow: -3px 0 6px rgba(0,0,0,0.45);
  }
  .page-card.right { box-shadow: 3px 0 6px rgba(0,0,0,0.45); }
  .green { background: var(--green); }
  .charcoal { background: var(--charcoal); }
  .slate { background: var(--slate); }
  .paper { background: var(--white); }

  .page-tab {
    position: absolute;
    top: 144px;
    height: 380px;
    width: 24px;
    background: var(--charcoal);
    border-radius: 12px;
    box-shadow: 0 0 5px rgba(0,0,0,0.5);
    writing-mode: vertical-rl;
    transform: rotate(180deg);
    display: flex;
    align-items: center;
    padding-top: 40px;
    color: var(--white);
    font-weight: 600;
    font-size: 13px;
    letter-spacing: 1.6px;
    text-transform: uppercase;
    white-space: nowrap;
  }
  .page-card.left .page-tab { left: 0; }
  .page-card.right .page-tab { right: 0; }
  .page-tab.short { padding-top: 100px; }

  .content-card {
    position: absolute;
    left: 206px;
    top: 10px;
    width: 913px;
    height: 655px;
    background: var(--white);
    border-radius: 22px;
    box-shadow: 0 0 10px rgba(0,0,0,0.5);
    text-align: center;
  }
  .slide-title {
    margin: 98px 0 0;
    color: var(--green);
    font-weight: 500;
    font-size: 51px;
    letter-spacing: 5px;
    line-height: 1;
  }
  .slide-body {
    width: 810px;
    margin: 78px auto 0;
    color: var(--body-grey);
    font-weight: 500;
    font-size: 22.5px;
    letter-spacing: 2.6px;
    line-height: 57px;
    text-transform: uppercase;
  }
  .brand-name {
    position: absolute;
    right: 48px;
    bottom: 44px;
    color: var(--logo-grey);
    font-weight: 400;
    font-size: 40px;
    letter-spacing: 1px;
  }
</style>
</head>
<body>
<main class="slide">
  <!-- right stack -->
  <div class="page-card right green" style="right:0"></div>
  <div class="page-card right charcoal" style="right:22px">
    <div class="page-tab">A Valuable Partnership</div>
  </div>
  <div class="page-card right slate" style="right:44px">
    <div class="page-tab short">Our Company</div>
  </div>

  <!-- left stack -->
  <nav class="section-stack">
    <div class="page-card left green" style="left:0"><div class="page-tab">Roll-Out Program</div></div>
    <div class="page-card left charcoal" style="left:22px"><div class="page-tab">Community Inolvement</div></div>
    <div class="page-card left slate" style="left:45px"><div class="page-tab short">Case Study</div></div>
    <div class="page-card left green" style="left:68px"><div class="page-tab">How We Are Different</div></div>
    <div class="page-card left slate" style="left:90px"><div class="page-tab">Program Overview</div></div>
    <div class="page-card left charcoal" style="left:112px"><div class="page-tab">Sample Program</div></div>
    <div class="page-card left green" style="left:135px"><div class="page-tab">Steps to Solution</div></div>
    <div class="page-card left paper" style="left:160px"></div>
    <div class="page-card left charcoal" style="left:184px"><div class="page-tab short" style="left:4px">The Problem</div></div>
  </nav>

  <section class="content-card">
    <h1 class="slide-title">Our Company</h1>
    <p class="slide-body">Lorem ipsum dolor sit amet, consectetur adi-piscing elit, sed do eiusmod tempor incididunt ut labore et dolore magna aliqua. Quis ipsum suspendisse ultrices gravida. Risus commodo viverra maecenas accumsan lacus vel facili-sis.</p>
    <div class="brand-name">BrightPath</div>
  </section>
</main>
</body>
</html>
```